Kestrane Energy b-card redesign

I would like to redesign the card (and power point template) for kestrane energy. We are a developer/owner/operator of high-tech biomass gasification power plants. We take ag waste like nut shells or fruit pits and convert that into electricity in the 1/2 - 3 MW range. I would like to change our company color from red to golden gate bridge orange (C=0,M=69,,Y=100,B=6).

```html
<!DOCTYPE html>
<html lang="en">
<head>
<meta charset="utf-8">
<title>Kestrane Energy – Business Card</title>
<link rel="stylesheet" href="https://fonts.googleapis.com/css2?family=Source+Sans+3:wght@400;600&display=swap">
<style>
  :root {
    --brand-orange: #e46b22;
    --band-orange: #e56b21;
    --ink: #1b1b1b;
    --paper: #ffffff;
    --band-text: #ffffff;
  }
  html, body {
    margin: 0;
    padding: 0;
    overflow: hidden;
    background: var(--paper);
  }
  .card {
    position: relative;
    width: 1200px;
    height: 686px;
    background: var(--paper);
    overflow: hidden;
    font-family: "Source Sans 3", sans-serif;
    color: var(--ink);
  }
  .wordmark {
    position: absolute;
    left: 111px;
    top: 128px;
    margin: 0;
    font-size: 50px;
    font-weight: 400;
    letter-spacing: 1px;
    color: var(--ink);
    line-height: 1;
  }
  .person {
    position: absolute;
    left: 96px;
    top: 316px;
  }
  .person-name {
    margin: 0;
    font-size: 31px;
    font-weight: 600;
    color: var(--brand-orange);
    line-height: 1.2;
  }
  .person-title {
    margin: 6px 0 0;
    font-size: 25px;
    font-weight: 400;
    color: var(--ink);
    letter-spacing: 0.5px;
    line-height: 1.2;
  }
  .contact-band {
    position: absolute;
    left: 0;
    top: 537px;
    width: 1200px;
    height: 149px;
    background: var(--band-orange);
    color: var(--band-text);
  }
  .contact-block {
    position: absolute;
    top: 42px;
    margin: 0;
    font-size: 23px;
    font-weight: 400;
    line-height: 34px;
    font-style: normal;
  }
  .contact-block span { display: block; }
  .contact-address { left: 96px; }
  .contact-phone { left: 495px; }
  .contact-online { left: 838px; }
  .divider {
    position: absolute;
    top: 44px;
    width: 4px;
    height: 61px;
    background: var(--band-text);
  }
  .divider-first { left: 422px; }
  .divider-second { left: 797px; }
</style>
</head>
<body>
  <main class="card">
    <h1 class="wordmark">Kestrane Energy</h1>

    <section class="person">
      <p class="person-name">Marcus Elliot Varden</p>
      <p class="person-title">CEO</p>
    </section>

    <footer class="contact-band">
      <address class="contact-block contact-address">
        <span>P.O. Box 48213</span>
        <span>Oakland, CA 94612</span>
      </address>
      <div class="divider divider-first"></div>
      <p class="contact-block contact-phone">
        <span>Phone: 415.555.0148</span>
        <span>Fax: 415.555.0193</span>
      </p>
      <div class="divider divider-second"></div>
      <p class="contact-block contact-online">
        <span>varden@kestraneenergy.net</span>
        <span>www.kestraneenergy.net</span>
      </p>
    </footer>
  </main>
</body>
</html>
```